existing Business Card Re design

We are wanting to re design our cards to reflect our new logo , i have attache the current business cards and new logo
i will need a business card that reflects the following information on each card.

card 1:
Harold Dunsby, President
555-382-9164
info@kpqfoamcoat.com

card 2:
Colin Thresher, Outside Sales
Office: 555-382-9164
Cell: 555-617-2048
Sales@kpqfoamcoat.com

Card 3
Louis Varcoe, Branch Manager
Office: 555-382-9164
Cell: 555-493-7752
Louis@kpqfoamcoat.com

Card 4
I will need a Generic card with no name on it just business
555-382-9164
info@kpqfoamcoat.com

Target Market(s)

Homeowners and Contractors

Contact Information for Business Card

We are wanting to re design our cards to reflect our new logo , i have attache the current business cards and new logo. same info on current card

card 1:
Harold Dunsby, President
555-382-9164
info@kpqfoamcoat.com

card 2:
Office: 555-382-9164
Cell: 555-617-2048
Sales@kpqfoamcoat.com

Card 3
Office: 555-382-9164
Cell: 555-493-7752
Louis@kpqfoamcoat.com

Card 4
555-382-9164
info@kpqfoamcoat.com

Requirements
Must have
• same info as current cards with a added business
"sanitizing"

```html
<!DOCTYPE html>
<html lang="en">
<head>
<meta charset="UTF-8">
<title>Peak Quality Foam – Business Card</title>
<link rel="stylesheet" href="https://fonts.googleapis.com/css2?family=Montserrat:wght@300;400;700&family=Oswald:wght@600&display=swap">
<style>
  :root {
    --backdrop: #d3d4cf;
    --card-white: #ffffff;
    --card-black: #242424;
    --brand-blue: #1a6fc4;
    --brand-navy: #0b2a5c;
    --ink: #1c1c1c;
    --emboss: #4a4a4a;
    --emboss-light: #5e5e5e;
  }
  * { box-sizing: border-box; margin: 0; padding: 0; }
  html, body {
    width: 1200px; height: 1058px; overflow: hidden;
    background: var(--backdrop);
    font-family: "Montserrat", sans-serif;
  }
  .stage { position: relative; width: 1200px; height: 1058px; }

  .card {
    position: absolute;
    width: 600px; height: 343px;
    box-shadow: 0 14px 30px rgba(0,0,0,0.18);
  }

  /* Front */
  .card--front {
    left: 70px; top: 170px;
    background: var(--card-white);
  }
  .brand {
    position: absolute; left: 0; right: 0; top: 78px;
    display: flex; justify-content: center; align-items: center; gap: 14px;
  }
  .brand__mark {
    width: 34px; height: 34px; background: var(--brand-navy);
  }
  .brand__name {
    font-family: "Montserrat", sans-serif; font-weight: 700;
    font-size: 30px; color: var(--brand-navy); letter-spacing: -0.3px;
  }
  .details {
    position: absolute; left: 46px; right: 40px; bottom: 62px;
    display: flex; align-items: center;
  }
  .person { width: 250px; text-align: right; padding-right: 26px; }
  .person__name {
    font-family: "Oswald", sans-serif; font-weight: 600;
    font-size: 32px; letter-spacing: 0.5px; color: var(--brand-blue);
    text-transform: uppercase; line-height: 1.1;
  }
  .person__title {
    font-weight: 300; font-size: 17px; color: var(--ink); margin-top: 2px;
  }
  .divider { width: 1.5px; height: 74px; background: var(--brand-blue); }
  .contact { list-style: none; padding-left: 24px; }
  .contact li {
    display: flex; align-items: center; gap: 10px;
    font-weight: 400; font-size: 15px; color: var(--ink); line-height: 1.55;
  }
  .contact svg { width: 11px; height: 11px; flex: none; }

  /* Back */
  .card--back {
    left: 540px; top: 580px;
    background: var(--card-black);
  }
  .brand--emboss { top: 150px; }
  .brand--emboss .brand__mark { background: var(--emboss); }
  .brand--emboss .brand__name { color: var(--emboss-light); }
</style>
</head>
<body>
<main class="stage">
  <section class="card card--front" aria-label="Business card front">
    <div class="brand">
      <span class="brand__mark"></span>
      <span class="brand__name">Peak Quality Foam</span>
    </div>
    <div class="details">
      <div class="person">
        <p class="person__name">Colin Thresher</p>
        <p class="person__title">Outside Sales</p>
      </div>
      <span class="divider"></span>
      <ul class="contact">
        <li>
          <svg viewBox="0 0 12 12" aria-hidden="true"><path d="M2.5 1 L4.5 1 L5 3.5 L3.8 4.5 C4.5 6 6 7.5 7.5 8.2 L8.5 7 L11 7.5 L11 9.5 C11 10.3 10.3 11 9.5 11 C5 11 1 7 1 2.5 C1 1.7 1.7 1 2.5 1Z" fill="var(--brand-blue)"/></svg>
          555-382-9164
        </li>
        <li>
          <svg viewBox="0 0 12 12" aria-hidden="true"><rect x="3" y="0.8" width="6" height="10.4" rx="1" fill="none" stroke="var(--brand-blue)" stroke-width="1.3"/><circle cx="6" cy="9.3" r="0.7" fill="var(--brand-blue)"/></svg>
          555-617-2048
        </li>
        <li>
          <svg viewBox="0 0 12 12" aria-hidden="true"><rect x="0.8" y="2.3" width="10.4" height="7.4" fill="none" stroke="var(--brand-blue)" stroke-width="1.2"/><path d="M1 2.6 L6 6.6 L11 2.6" fill="none" stroke="var(--brand-blue)" stroke-width="1.2"/></svg>
          Sales@kpqfoamcoat.com
        </li>
      </ul>
    </div>
  </section>

  <section class="card card--back" aria-label="Business card back">
    <div class="brand brand--emboss">
      <span class="brand__mark"></span>
      <span class="brand__name">Peak Quality Foam</span>
    </div>
  </section>
</main>
</body>
</html>
```